依頼詳細
留学生向けのアルバイト募集のA4チラシ(印刷後壁に貼り付け)を作成します。複数の企業が参加し、共通のテンプレートを使用し、1店舗(例:xx居酒屋 xx店)1枚で印刷します。そこでその雛形のデザインをお願いしたいと思います。
レイアウトは添付ファイルにこだわる必要はないです。
*どのような業種職種でも使える汎用性の高いデザインでお願いします。
記載項目
ロゴ(写真データ)/紹介写真(写真データ)店名/業種/給与/勤務時間/最寄駅/PR文/応募条件/応募連絡先/先輩の声/先輩の写真(写真データ)/名前/出身/年齢/日本語レベル/在日期間
また、テキスト入力の部分は名前/出身/年齢/日本語レベル/在日期間を除く全ての部分にふりがなを付けられるようにしてください。(添付ファイル参照)

写真データ以外は全てテキストデータで入力

```html
<!DOCTYPE html>
<html lang="ja">
<head>
<meta charset="utf-8">
<title>アルバイト募集 Job Information</title>
<link rel="stylesheet" href="https://fonts.googleapis.com/css2?family=Noto+Sans+JP:wght@400;700;900&family=Permanent+Marker&display=swap">
<style>
:root{
  --ink:#111;
  --page:#0d0d0d;
  --panel:#fff;
  --bar:#3b3b3b;
  --bar-text:#fff;
  --accent-green:#6fbf2a;
  --accent-red:#c8161d;
  --caption:#f6e7a8;
  --photo-a:#8a5a33;
  --photo-b:#d8b07a;
  --person-a:#6e6258;
  --person-b:#c9bfb3;
  --line:#9a9a9a;
}
*{margin:0;padding:0;box-sizing:border-box}
html,body{width:849px;height:1200px;overflow:hidden;background:var(--page)}
body{font-family:"Noto Sans JP",sans-serif;color:var(--ink)}
.flyer{position:relative;width:849px;height:1200px;background:var(--page)}
rt{font-size:.42em;font-weight:400;letter-spacing:.05em}
.header{position:absolute;left:0;top:0;width:849px;height:104px;background:#000}
.brush-band{position:absolute;left:210px;top:8px;width:630px;height:92px;border-radius:40px 10px 50px 14px;
  background:linear-gradient(100deg,#1f3a0c 0%,var(--accent-green) 35%,#4a8e1a 70%,#1d330b 100%)}
.title{position:absolute;left:20px;top:10px;color:#fff;font-weight:900;font-size:40px;letter-spacing:2px}
.title rt{font-size:12px}
.job-info{position:absolute;left:360px;top:6px;color:#fff;font-family:"Permanent Marker",cursive;font-size:56px;line-height:1;transform:rotate(-6deg);transform-origin:left}
.job-info span{display:block;margin-left:40px}
.job-no{position:absolute;left:12px;top:114px;background:var(--accent-red);color:#fff;font-weight:700;font-size:15px;padding:2px 10px}
.name-bar{position:absolute;left:105px;top:108px;width:735px;height:22px;background:var(--bar);color:#fff;text-align:center;font-size:13px;letter-spacing:10px;line-height:22px}
.name-row{position:absolute;left:105px;top:130px;width:735px;height:78px;background:var(--panel);text-align:center}
.store-name{font-weight:900;font-size:34px;line-height:78px;padding-top:6px}
.store-name rt{font-size:11px}
.logo{position:absolute;left:24px;top:140px;width:72px;height:72px;border-radius:50%;background:#fff;border:4px solid #000;display:flex;align-items:center;justify-content:center;font-weight:900;font-size:18px}
.photo{position:absolute;left:23px;top:221px;width:396px;height:303px;background:linear-gradient(160deg,var(--photo-b),var(--photo-a))}
.caption{position:absolute;left:40px;top:228px;background:var(--caption);color:var(--accent-red);font-weight:900;font-size:16px;padding:4px 12px;border-radius:16px}
.info{position:absolute;left:430px;width:396px;background:var(--panel)}
.bar{background:var(--bar);color:var(--bar-text);font-size:13px;font-weight:700;text-align:center;letter-spacing:4px;height:22px;line-height:22px}
.info .body{padding:6px 14px;font-size:15px;line-height:1.9;font-weight:700}
.info .body rt{font-size:9px}
.wide{position:absolute;left:23px;width:803px;background:var(--panel)}
.wide .body{padding:6px 18px;font-size:16px;line-height:2.1;font-weight:700}
.wide .body rt{font-size:9px}
.wide .center{text-align:center}
.voice{position:absolute;top:937px;width:396px;height:253px;background:var(--panel)}
.voice .person{position:absolute;left:6px;top:30px;width:128px;height:122px;background:linear-gradient(180deg,var(--person-b),var(--person-a))}
.voice table{position:absolute;left:140px;top:30px;width:250px;border-collapse:collapse;font-size:13px}
.voice td{border:1px solid var(--line);padding:2px 6px;height:24px}
.voice td:first-child{width:84px;background:#eee;font-size:12px}
.voice .quote{position:absolute;left:8px;top:160px;width:380px;font-size:12px;line-height:1.6}
</style>
</head>
<body>
<main class="flyer">
  <header class="header">
    <div class="brush-band" role="img" aria-label="緑色のブラシストローク装飾"></div>
    <h1 class="title">アルバイト<ruby>募集<rt>ぼしゅう</rt></ruby></h1>
    <div class="job-info">Job<span>information!</span></div>
  </header>

  <div class="job-no">Job No.1</div>
  <div class="name-bar">店名</div>
  <div class="name-row">
    <div class="store-name"><ruby>○○居酒屋××店<rt>マルマルイザカヤ バツバツテン</rt></ruby></div>
  </div>
  <div class="logo">○○亭</div>

  <div class="photo" role="img" aria-label="店内で働くスタッフの写真"></div>
  <div class="caption">先輩留学生も働いている安心の仕事場！</div>

  <section class="info" style="top:229px;height:125px">
    <div class="bar">業種・給与</div>
    <div class="body">
      <div><ruby>業種<rt>ギョウシュ</rt></ruby>：<ruby>飲食店<rt>インショクテン</rt></ruby>・<ruby>キッチン<rt></rt></ruby></div>
      <div style="padding-left:80px">ホール：¥1,000/h</div>
      <div style="padding-left:80px">キッチン：¥980/h</div>
    </div>
  </section>
  <section class="info" style="top:362px;height:68px">
    <div class="bar">勤務時間</div>
    <div class="body" style="text-align:center"><ruby>平日<rt>ヘイジツ</rt></ruby>夕方：6:30〜24:00</div>
  </section>
  <section class="info" style="top:439px;height:85px">
    <div class="bar">最寄駅</div>
    <div class="body" style="text-align:center;padding-top:14px"><ruby>青葉・桜丘・青葉見附駅<rt>アオバ・サクラガオカ・アオバミツケ</rt></ruby></div>
  </section>

  <section class="wide" style="top:540px;height:140px">
    <div class="bar">P R 文</div>
    <div class="body">
      <div><ruby>留学生大歓迎<rt>リュウガクセイダイカンゲイ</rt></ruby>！<ruby>日本語<rt>ニホンゴ</rt></ruby>があまり<ruby>喋<rt>シャベ</rt></ruby>ることができなくても、<ruby>日本語<rt>ニホンゴ</rt></ruby>レベルに<ruby>合<rt>ア</rt></ruby>わせた<ruby>研修<rt>ケンシュウ</rt></ruby><ruby>有<rt>ア</rt></ruby>り。</div>
      <div><ruby>学校<rt>ガッコウ</rt></ruby>に<ruby>行<rt>イ</rt></ruby>きながらでも<ruby>無理<rt>ムリ</rt></ruby>なく<ruby>働<rt>ハタラ</rt></ruby>ける<ruby>平日<rt>ヘイジツ</rt></ruby>6:30〜10:00シフトも<ruby>可能<rt>カノウ</rt></ruby>！</div>
    </div>
  </section>

  <section class="wide" style="top:688px;height:124px">
    <div class="bar">応募条件</div>
    <div class="body center" style="line-height:1.9">
      <div>ホール：<ruby>N4以上<rt>イジョウ</rt></ruby>（<ruby>応相談<rt>オウソウダン</rt></ruby>）</div>
      <div>キッチン：<ruby>N4以上<rt>イジョウ</rt></ruby>（<ruby>応相談<rt>オウソウダン</rt></ruby>）</div>
      <div><ruby>応募資格<rt>オウボシカク</rt></ruby>：<ruby>N3以上<rt>イジョウ</rt></ruby>（<ruby>応相談<rt>オウソウダン</rt></ruby>）</div>
    </div>
  </section>

  <section class="wide" style="top:820px;height:110px">
    <div class="bar">応募先</div>
    <div class="body center" style="line-height:1.7">
      <div><ruby>株式会社XXX アルバイト採用係<rt>カブシキガイシャ アルバイトサイヨウガカリ</rt></ruby></div>
      <div>東京都みどり区xxxxxxxx　TEL.03-xxx-xxx</div>
    </div>
  </section>

  <section class="voice" style="left:23px">
    <div class="bar">先輩からの一言</div>
    <div class="person" role="img" aria-label="先輩スタッフの写真"></div>
    <table>
      <tr><td>名前</td><td>ミンさん</td></tr>
      <tr><td>出身</td><td>ベトナム</td></tr>
      <tr><td>年齢</td><td>22歳</td></tr>
      <tr><td>日本語検定</td><td>3級</td></tr>
      <tr><td>在日期間</td><td>1年</td></tr>
    </table>
    <p class="quote">最初は不安でしたが、先輩が丁寧に教えてくれて安心して働くことができています。お客様を楽しくお迎えする毎日がとても楽しいです。日本語も上達しました！</p>
  </section>

  <section class="voice" style="left:430px">
    <div class="bar">先輩からの一言</div>
    <div class="person" role="img" aria-label="先輩スタッフの写真"></div>
    <table>
      <tr><td>名前</td><td>リンさん</td></tr>
      <tr><td>出身</td><td>台湾</td></tr>
      <tr><td>年齢</td><td>24歳</td></tr>
      <tr><td>日本語検定</td><td>1級</td></tr>
      <tr><td>在日期間</td><td>0.5年</td></tr>
    </table>
    <p class="quote">日本語を実際に仕事をしながら学びたくて始めました。職場の雰囲気がとても良く、シフトも学校に合わせて相談できます。一緒に頑張りましょう！</p>
  </section>
</main>
</body>
</html>
```